Wine Label Design

A wine label for 750ml bottles. Same label for different varieties with the variety / region / vintage to be updated as required.
Brand: Beyond the Ridge
Product Use: Front and Back label suitable for a 750 ml bottle (preferably Burgundy bottles)
Design Brief: Beyond the Ridge is a small winery that produces limited amounts of hand crafted wines that are aimed at the mid to top end of the market and requires a label befitting the work that goes into the creation of the wine. In terms of style i don't have any preconceptions and am open to a broad range of design suggestions at the same level of existing premium brands or innovative brands.
Must Have for Front label
Front Label
Beyond the Ridge
2013
Grampians
Shiraz
750ML (should be in smaller text)
Alc. 14% by Vol. (should be in smaller text)
Must Have for Back Label
Beyond the Ridge
2013
Grampians
Shiraz
www.beyondtheridge.com.au (should be in smaller text)
Product of Australia
Alc.14% by Vol. (should be in smaller text)
Contains preservative 220(should be in smaller text)
Below are some guides for dimensions:
The Front Label Size can be between
100 - 120 mm (Width) x 70 - 85 mm (Height)
The back label size can be between
90 mm (Width) x 70 - 85 mm (Height)
Target Market(s)
Medium to top end of the wine market who require the label to be a reflection of the wine.
Industry/Entity Type
Product
Colors
Designer to choose colors to be used in the design.
Look and feel

```html
<!DOCTYPE html>
<html lang="en">
<head>
<meta charset="utf-8">
<title>Beyond the Ridge — Grampians Shiraz 2013</title>
<link rel="stylesheet" href="https://fonts.googleapis.com/css2?family=Poiret+One&display=swap">
<style>
  :root {
    --paper: #f3efe7;
    --paper-edge: #e9e3d8;
    --ink: #111111;
    --ink-soft: #3a3838;
    --flourish: #cfc7bc;
    --frame: #141414;
  }
  * { box-sizing: border-box; margin: 0; padding: 0; }
  html, body {
    width: 1200px;
    height: 1109px;
    overflow: hidden;
    background: var(--paper);
  }
  .label {
    position: relative;
    width: 1200px;
    height: 1109px;
    background: radial-gradient(ellipse at 50% 45%, var(--paper) 55%, var(--paper-edge) 100%);
    border: 10px solid var(--frame);
    font-family: "Poiret One", "Futura", sans-serif;
    color: var(--ink);
    overflow: hidden;
  }
  .label__flourish {
    position: absolute;
    inset: 0;
    width: 100%;
    height: 100%;
  }
  .label__line {
    position: absolute;
    left: 0;
    width: 100%;
    text-align: center;
    line-height: 1;
    white-space: nowrap;
  }
  .brand-name {
    top: 52px;
    font-size: 124px;
    letter-spacing: 1px;
    color: var(--ink);
  }
  .brand-rule {
    position: absolute;
    left: 112px;
    width: 956px;
    background: var(--ink);
  }
  .brand-rule--top { top: 212px; height: 5px; }
  .brand-rule--bottom { top: 224px; height: 3px; }
  .vintage {
    top: 330px;
    font-size: 104px;
    color: var(--ink-soft);
  }
  .region {
    top: 626px;
    font-size: 58px;
    color: var(--ink-soft);
  }
  .variety {
    top: 734px;
    font-size: 58px;
    color: var(--ink-soft);
  }
  .details {
    position: absolute;
    top: 858px;
    left: 0;
    width: 100%;
    text-align: center;
    font-size: 22px;
    line-height: 40px;
    color: var(--ink-soft);
    list-style: none;
  }
</style>
</head>
<body>
  <main class="label">
    <svg class="label__flourish" viewBox="0 0 1180 1089" role="img" aria-label="Faint baroque acanthus scroll ornament sweeping diagonally from lower left to upper right">
      <defs>
        <linearGradient id="flourish-tone" x1="0" y1="1" x2="1" y2="0">
          <stop offset="0" stop-color="var(--flourish)" stop-opacity="0.55"/>
          <stop offset="0.5" stop-color="var(--flourish)" stop-opacity="0.35"/>
          <stop offset="1" stop-color="var(--flourish)" stop-opacity="0.55"/>
        </linearGradient>
      </defs>
      <path d="M40 900 C 220 760, 420 700, 560 560 C 700 420, 860 300, 1120 60 L 1150 200 C 960 340, 820 470, 690 590 C 560 710, 360 820, 90 990 Z" fill="url(#flourish-tone)"/>
    </svg>

    <h1 class="label__line brand-name">Beyond the Ridge</h1>
    <div class="brand-rule brand-rule--top"></div>
    <div class="brand-rule brand-rule--bottom"></div>

    <p class="label__line vintage">2013</p>
    <p class="label__line region">Grampians</p>
    <p class="label__line variety">Shiraz</p>

    <ul class="details">
      <li>www.beyondtheridge.com.au</li>
      <li>Product of Australia</li>
      <li>750ML</li>
      <li>Alc.14% by Vol.</li>
      <li>Contains preservative 220</li>
    </ul>
  </main>
</body>
</html>
```